WEBSITE & LOGO for MEDICAL CILINC

BRAND NAME ( LUMORA) Medical clinic for intravenous (IV) vitamin hydration and wellness therapy. range of signature infusions and boosters are targeted at preventative health and wellness – essentially replenishing your body with the fluids and vitamins it needs to be in tip-top condition.

Blood testing
laboratory analysis
IV therapy
IV infusion drips
phlebotomy services
nurses for Home care services
Patient repatriation services to their countries
Hire of medical equipments including beds and wheel chairs

www.quellant.com
www.brisoclinic.com
http://fundoroplan.co.uk

All adults
18+ women and men.

No black color in the background
DNA double helix image should to be implemented in the design and logo.
the website should be easy to be used so the clients can add to the shopping cart
- select treatment or drips
- supplement
- book nurses
- book home visit
- book nurse for international home care journey

Colors
86cae7
33b8a4
e4daeb
f9d9e8
fefafc
fbd2d3
eee9f4
85acd3
0455a3

Requirements
Must have
• DNA Double helix in Java animation
injection icon for IV injection
Infusion Icon Bag for IV infusion
Analysis icon
phlebotomy services icon
Patient repatriation services icon
Hire of medical equipments icon

light background and water blue menu and buttons with highlights
Nice to have
• dynamic website where
IV injections scroll from side to side
IV infusion scroll from side to side.

```html
<!DOCTYPE html>
<html lang="en">
<head>
<meta charset="utf-8">
<title>Lumora – IV Vitamin Hydration &amp; Wellness Therapy</title>
<link href="https://fonts.googleapis.com/css2?family=Lato:wght@400;700;900&display=swap" rel="stylesheet">
<style>
:root{
  --teal:#33b8a4;
  --navy:#0455a3;
  --sky:#86cae7;
  --steel:#85acd3;
  --lavender:#e4daeb;
  --lavender-soft:#eee9f4;
  --ink:#1c2330;
  --text:#555b66;
  --line:#dfe3e8;
  --footer-bg:#f3f4f6;
  --forest:#0c4b52;
}
*{box-sizing:border-box;margin:0;padding:0}
html,body{width:1200px;height:4942px;overflow:hidden}
body{position:relative;background:#fff;font-family:"Lato",sans-serif;color:var(--text)}
.abs{position:absolute}
.btn{position:absolute;display:flex;align-items:center;justify-content:center;border-radius:30px;font-weight:700;font-size:13px;text-transform:uppercase;letter-spacing:.2px}
.btn-solid{background:var(--teal);color:#fff;box-shadow:0 4px 10px rgba(51,184,164,.35)}
.btn-outline{border:2px solid var(--navy);color:var(--navy);background:#fff}

/* header */
.site-header{position:absolute;left:0;top:0;width:1200px;height:130px;background:#fff}
.brand{position:absolute;display:flex;align-items:center;gap:12px;font-weight:700;color:var(--ink)}
.brand .mark{width:30px;height:30px;border-radius:50%;background:var(--teal)}
.call{position:absolute;left:440px;top:14px;display:flex;gap:10px;align-items:center}
.call .ico{width:32px;height:32px;border-radius:50%;background:var(--navy);display:flex;align-items:center;justify-content:center}
.call small{display:block;font-size:14px;color:var(--ink)}
.call strong{display:block;font-size:19px;color:var(--navy);font-weight:900}
.main-nav{position:absolute;left:410px;top:90px;display:flex;gap:32px;font-size:14px;font-weight:700;color:var(--ink)}
.main-nav .active{color:var(--teal)}
.cart{position:absolute;left:1020px;top:15px;width:36px;height:36px;border:2px solid var(--navy);border-radius:50%;display:flex;align-items:center;justify-content:center}

/* hero */
.hero{position:absolute;left:0;top:130px;width:1200px;height:690px;overflow:hidden}
.hero-photo{position:absolute;inset:0;background:
  radial-gradient(ellipse 260px 420px at 420px 330px,rgba(120,170,230,.55),rgba(120,170,230,0) 70%),
  radial-gradient(ellipse 380px 460px at 300px 420px,rgba(240,244,250,.9),rgba(240,244,250,0) 70%),
  radial-gradient(ellipse 420px 300px at 1000px 200px,rgba(255,255,255,.85),rgba(255,255,255,0) 70%),
  linear-gradient(100deg,#41679e 0%,#7d9cc6 22%,#c3d3e6 45%,#9fb8d6 62%,#d9e3ee 80%,#aebfd4 100%)}
.hero h1{position:absolute;left:836px;top:150px;font-size:62px;font-weight:900;color:#1b2230;letter-spacing:1px}
.hero p{position:absolute;left:840px;top:230px;font-size:24px;line-height:31px;color:#1b2230;width:250px}
.dots{position:absolute;left:840px;top:418px;display:flex;gap:8px}
.dots span{width:12px;height:12px;border-radius:50%;border:2px solid #222}
.dots span.on{background:var(--teal);border-color:var(--teal)}

/* services */
.sec-title{position:absolute;left:0;width:1200px;text-align:center;font-weight:700;color:var(--ink)}
.sec-title::after{content:"";display:block;width:56px;height:3px;background:var(--teal);margin:14px auto 0}
.service-card{position:absolute;width:284px;height:365px;background:#fff;border:1px solid var(--line);text-align:center}
.service-card .photo{height:190px}
.service-card .badge{position:absolute;left:102px;top:150px;width:80px;height:80px;border-radius:50%;background:var(--teal);border:4px solid #fff;display:flex;align-items:center;justify-content:center}
.service-card h3{margin-top:62px;font-size:15px;font-weight:900;color:var(--ink)}
.service-card p{margin:12px auto 0;width:240px;font-size:13.5px;line-height:21px}
.tone-lab{background:radial-gradient(ellipse at 30% 40%,#5d86b8,rgba(93,134,184,0) 60%),linear-gradient(135deg,#e6edf3,#a7bfd6)}
.tone-white{background:radial-gradient(ellipse at 60% 40%,#b7c4d0,rgba(183,196,208,0) 60%),linear-gradient(135deg,#f2f4f6,#cfd7df)}
.tone-room{background:radial-gradient(ellipse at 40% 60%,#8a6b5f,rgba(138,107,95,0) 50%),linear-gradient(135deg,#eef0f3,#c9cfd8)}
.tone-garden{background:radial-gradient(ellipse at 30% 30%,#c94d4d,rgba(201,77,77,0) 45%),radial-gradient(ellipse at 80% 60%,#8fd0c6,rgba(143,208,198,0) 50%),linear-gradient(135deg,#8fb37a,#d7e2cf)}
.faint-helix{position:absolute;background:radial-gradient(ellipse,rgba(190,196,208,.4),rgba(255,255,255,0) 70%)}

/* welcome */
.welcome{position:absolute;left:0;top:1935px;width:1200px;height:552px;background:#fcf6f9}
.welcome .photo{position:absolute;left:0;top:0;width:618px;height:552px;background:
  radial-gradient(ellipse 150px 230px at 300px 300px,rgba(92,196,190,.85),rgba(92,196,190,0) 70%),
  radial-gradient(ellipse 120px 200px at 460px 260px,rgba(245,247,249,.9),rgba(245,247,249,0) 70%),
  linear-gradient(135deg,#c9d6dc 0%,#e7eef0 45%,#b9ccd3 100%)}
.welcome h2{position:absolute;left:703px;top:112px;font-size:28px;font-weight:900;color:var(--ink)}
.welcome p{position:absolute;left:703px;top:170px;width:362px;font-size:13px;line-height:24px}

/* journey band */
.journey{position:absolute;left:0;top:2487px;width:1200px;height:560px;overflow:hidden}
.journey .photo{position:absolute;inset:0;background:
  radial-gradient(ellipse 260px 180px at 850px 170px,rgba(110,210,230,.5),rgba(110,210,230,0) 70%),
  radial-gradient(ellipse 200px 300px at 1120px 200px,rgba(235,242,250,.75),rgba(235,242,250,0) 70%),
  linear-gradient(100deg,#0a2f8d 0%,#0e4aa5 45%,#1f6cb3 70%,#5d9ccc 100%)}
.journey h2{position:absolute;left:143px;top:130px;font-size:37px;line-height:48px;font-weight:900;color:#fff}

/* testimonials */
.testimonial{position:absolute;top:3205px;width:287px;height:326px;background:var(--lavender-soft);border:1px solid #d6cde2;border-radius:4px;text-align:center}
.testimonial h4{margin-top:40px;font-size:18px;font-weight:700;color:var(--ink)}
.testimonial small{display:block;margin-top:6px;font-size:13px}
.testimonial p{margin:14px auto 0;width:245px;font-size:13.5px;line-height:21px}
.testimonial .avatar{position:absolute;left:92px;top:232px;width:104px;height:104px;border-radius:50%;border:4px solid #fff;background:radial-gradient(circle at 50% 40%,#d9a98a,#7a4e3a 75%)}
.arrow{position:absolute;top:3352px}

/* blog */
.blog{position:absolute;left:0;top:3648px;width:1200px;height:860px;overflow:hidden}
.blog .photo{position:absolute;inset:0;background:
  radial-gradient(ellipse 400px 200px at 250px 120px,rgba(120,200,200,.35),rgba(120,200,200,0) 70%),
  linear-gradient(180deg,#24a6a3 0%,#1f8fa9 45%,#1a63a6 85%)}
.blog-card{position:absolute;width:287px;background:#fff;border-radius:4px;overflow:hidden}
.blog-card .photo-s{height:200px}
.blog-card .date{position:absolute;right:14px;top:14px;width:46px;height:46px;border-radius:50%;background:var(--teal);color:#fff;font-size:10px;font-weight:900;line-height:12px;display:flex;align-items:center;justify-content:center;text-align:center}
.blog-card h3{margin:26px 22px 0;font-size:14px;font-weight:900;color:var(--ink);line-height:19px}
.blog-card p{margin:12px 22px 0;font-size:13px;line-height:21px}
.blog-card .more{display:inline-flex;margin:16px 22px 26px;padding:7px 18px;border:2px solid var(--navy);border-radius:20px;font-size:11px;font-weight:900;color:var(--navy)}

/* footer */
.site-footer{position:absolute;left:0;top:4470px;width:1200px;height:360px;background:var(--footer-bg)}
.field{position:absolute;left:143px;width:273px;height:36px;background:#fff;border:1px solid var(--line);font-size:11px;padding:11px 14px;color:#777}
.foot-h{position:absolute;font-size:17px;font-weight:900;color:var(--ink)}
.foot-list{position:absolute;list-style:none;font-size:13.5px;line-height:26.5px}
.contact-row{position:absolute;left:470px;display:flex;gap:14px;font-size:13.5px;line-height:19px}
.social{position:absolute;left:945px;list-style:none;font-size:13.5px;color:var(--navy)}
.social li{display:flex;align-items:center;gap:10px;height:41px}
.social i{width:28px;height:28px;border:1.5px solid var(--navy);border-radius:50%}
.copyright{position:absolute;left:0;top:4880px;width:1200px;text-align:center;font-size:13px;color:var(--ink)}
</style>
</head>
<body>

<header class="site-header">
  <div class="brand" style="left:145px;top:36px;font-size:40px"><span class="mark"></span>Lumora</div>
  <div class="call">
    <span class="ico"><svg width="16" height="16" viewBox="0 0 24 24"><path fill="#fff" d="M6.6 10.8a15 15 0 006.6 6.6l2.2-2.2a1 1 0 011-.25 11.4 11.4 0 003.6.57 1 1 0 011 1V20a1 1 0 01-1 1A17 17 0 013 4a1 1 0 011-1h3.5a1 1 0 011 1c0 1.25.2 2.45.57 3.57a1 1 0 01-.25 1z"/></svg></span>
    <div><small>Call Us :</small><strong>(555) 0142-7780</strong></div>
  </div>
  <div class="btn btn-solid" style="left:659px;top:14px;width:148px;height:38px;font-size:12px">Book Nurses</div>
  <div class="btn btn-outline" style="left:818px;top:14px;width:190px;height:38px;font-size:12px">Book Home Visit</div>
  <div class="cart"><svg width="16" height="16" viewBox="0 0 24 24"><path d="M3 4h3l2.5 10h10l2-7H8" stroke="#0455a3" stroke-width="2" fill="none"/><circle cx="10" cy="19" r="1.8" fill="#0455a3"/><circle cx="17" cy="19" r="1.8" fill="#0455a3"/></svg></div>
  <nav class="main-nav">
    <span class="active">HOME</span><span>ABOUT US</span><span>TREATMENT</span><span>OUR SERVICES</span><span>SUPPLEMENT</span><span>CONTACT US</span>
  </nav>
</header>

<section class="hero">
  <div class="hero-photo" role="img" aria-label="Clinician in a white coat touching a glowing blue DNA double helix against a cloudy blue sky"></div>
  <h1>LUMORA</h1>
  <p>Intravenous (IV) vitamin hydration and wellness therapy</p>
  <div class="btn btn-solid" style="left:840px;top:348px;width:160px;height:38px;font-size:12px">Book Nurses</div>
  <div class="dots"><span class="on"></span><span></span><span></span><span></span></div>
  <svg class="abs" style="left:0;top:560px" width="1200" height="130" viewBox="0 0 1200 130" preserveAspectRatio="none">
    <path d="M0 60 C250 120 520 130 760 80 C930 45 1080 20 1200 40 L1200 130 L0 130Z" fill="#fff"/>
    <path d="M0 50 C250 115 520 120 760 70 C930 35 1080 12 1200 30" fill="none" stroke="#33b8a4" stroke-width="7"/>
  </svg>
</section>

<div class="faint-helix" role="img" aria-label="Faint grey DNA double helix in the background" style="left:0;top:1050px;width:260px;height:760px"></div>
<div class="faint-helix" role="img" aria-label="Faint grey DNA double helix in the background" style="left:380px;top:1020px;width:360px;height:700px"></div>
<div class="faint-helix" role="img" aria-label="Faint grey DNA double helix in the background" style="left:960px;top:980px;width:240px;height:560px"></div>

<h2 class="sec-title" style="top:866px;font-size:38px">Our Services</h2>

<article class="service-card" style="left:143px;top:973px">
  <div class="photo tone-lab" role="img" aria-label="Gloved hands holding blood sample tubes"></div>
  <div class="badge"><svg width="34" height="34" viewBox="0 0 24 24" fill="none" stroke="#fff" stroke-width="1.6"><path d="M9 3h6M10 3v14a2 2 0 004 0V3"/><path d="M10 11h4"/></svg></div>
  <h3>BLOOD TESTING</h3>
  <p>Sed ut perspiciatis unde omnis iste natus error sit voluptatem accium doloremque laudantium</p>
</article>
<article class="service-card" style="left:457px;top:983px">
  <div class="photo tone-white" role="img" aria-label="Lab technician looking through a microscope"></div>
  <div class="badge"><svg width="34" height="34" viewBox="0 0 24 24" fill="none" stroke="#fff" stroke-width="1.6"><path d="M8 20h10M10 20v-3M9 4l4 2-3 6-4-2z"/><path d="M14 9a5 5 0 01-1 9"/></svg></div>
  <h3>LABORATORY ANALYSIS</h3>
  <p>Sed ut perspiciatis unde omnis iste natus error sit voluptatem accium doloremque laudantium</p>
</article>
<article class="service-card" style="left:771px;top:973px">
  <div class="photo tone-room" role="img" aria-label="Patient receiving IV therapy from a nurse"></div>
  <div class="badge"><svg width="34" height="34" viewBox="0 0 24 24" fill="none" stroke="#fff" stroke-width="1.6"><path d="M7 3h10v8a5 5 0 01-10 0z"/><path d="M12 16v5"/></svg></div>
  <h3>IV THERAPY</h3>
  <p>Sed ut perspiciatis unde omnis iste natus error sit voluptatem accium doloremque laudantium</p>
</article>
<article class="service-card" style="left:143px;top:1367px">
  <div class="photo tone-lab" role="img" aria-label="Nurse adjusting an IV infusion drip bag for a patient"></div>
  <div class="badge"><svg width="34" height="34" viewBox="0 0 24 24" fill="none" stroke="#fff" stroke-width="1.6"><path d="M4 20l3-3M6 13l5 5M8 11l8-8 5 5-8 8z"/></svg></div>
  <h3>IV INFUSION DRIPS</h3>
  <p>Sed ut perspiciatis unde omnis iste natus error sit voluptatem accium doloremque laudantium</p>
</article>
<article class="service-card" style="left:457px;top:1377px">
  <div class="photo tone-white" role="img" aria-label="Arm prepared for a blood draw"></div>
  <div class="badge"><svg width="34" height="34" viewBox="0 0 24 24" fill="none" stroke="#fff" stroke-width="1.6"><path d="M12 3c3 4 5 7 5 10a5 5 0 01-10 0c0-3 2-6 5-10z"/></svg></div>
  <h3>PHLEBOTOMY SERVICES</h3>
  <p>Sed ut perspiciatis unde omnis iste natus error sit voluptatem accium doloremque laudantium</p>
</article>
<article class="service-card" style="left:771px;top:1367px">
  <div class="photo tone-garden" role="img" aria-label="Home care nurse assisting an elderly woman in a wheelchair outdoors"></div>
  <div class="badge"><svg width="34" height="34" viewBox="0 0 24 24" fill="none" stroke="#fff" stroke-width="1.6"><circle cx="12" cy="8" r="4"/><path d="M4 21a8 8 0 0116 0"/><path d="M12 15v4M10 17h4"/></svg></div>
  <h3>NURSES FOR HOME CARE</h3>
  <p>Sed ut perspiciatis unde omnis iste natus error sit voluptatem accium doloremque laudantium</p>
</article>

<div class="btn btn-outline" style="left:472px;top:1804px;width:257px;height:44px;font-size:13px">View More Services</div>

<section class="welcome">
  <div class="photo" role="img" aria-label="Smiling nurse in teal scrubs holding a clipboard in a hospital corridor"></div>
  <h2>WELCOME TO LUMORA</h2>
  <p>Sed ut perspiciatis unde omnis iste natus error sit voluptatem accusantium doloremque laudantium, totam rem aperiam, eaque ipsa quae ab illo inventore veritatis et quasi architecto beatae vitae dicta sunt explicabo. Nemo enim ipsam voluptatem quia voluptas sit aspernatur aut odit aut fugit, sed quia cnsequuntur magni dolores eos qui ratione voluptatem sequi nesciunt. Neque porro quisquam est</p>
  <div class="btn btn-solid" style="left:703px;top:393px;width:167px;height:44px">Learn More</div>
</section>

<section class="journey">
  <div class="photo" role="img" aria-label="Doctor holding a tablet with a holographic DNA double helix and molecule graphics on deep blue"></div>
  <h2>BOOK NURSE FOR<br>INTERNATIONAL<br>HOME CARE JOURNEY</h2>
  <div class="btn btn-solid" style="left:145px;top:295px;width:203px;height:50px;font-size:16px">Book Nurses</div>
  <svg class="abs" style="left:0;top:400px" width="1200" height="160" viewBox="0 0 1200 160" preserveAspectRatio="none">
    <path d="M0 70 C220 130 520 140 760 90 C950 50 1100 40 1200 55 L1200 160 L0 160Z" fill="#fff"/>
    <path d="M0 60 C220 122 520 130 760 80 C950 40 1100 30 1200 45" fill="none" stroke="#33b8a4" stroke-width="7"/>
  </svg>
</section>

<h2 class="sec-title" style="top:3095px;font-size:38px">Client Testimonials</h2>
<svg class="arrow" style="left:100px" width="20" height="28" viewBox="0 0 20 28"><path d="M15 3L5 14l10 11" fill="none" stroke="#444" stroke-width="3"/></svg>
<svg class="arrow" style="left:1082px" width="20" height="28" viewBox="0 0 20 28"><path d="M5 3l10 11L5 25" fill="none" stroke="#444" stroke-width="3"/></svg>
<article class="testimonial" style="left:143px">
  <h4>Mara Okonjo</h4><small>Lumora</small>
  <p>Sed ut perspiciatis unde omnis iste natus error sit voluptatem accium doloremque laudantium, totam rem aperiam, eaque ipsa quae ab illo inventore veritatis et quasi archecto beatae vitae dicta sunt.</p>
  <div class="avatar" role="img" aria-label="Client portrait"></div>
</article>
<article class="testimonial" style="left:457px">
  <h4>Mara Okonjo</h4><small>Lumora</small>
  <p>Sed ut perspiciatis unde omnis iste natus error sit voluptatem accium doloremque laudantium, totam rem aperiam, eaque ipsa quae ab illo inventore veritatis et quasi archecto beatae vitae dicta sunt.</p>
  <div class="avatar" role="img" aria-label="Client portrait"></div>
</article>
<article class="testimonial" style="left:767px">
  <h4>Mara Okonjo</h4><small>Lumora</small>
  <p>Sed ut perspiciatis unde omnis iste natus error sit voluptatem accium doloremque laudantium, totam rem aperiam, eaque ipsa quae ab illo inventore veritatis et quasi archecto beatae vitae dicta sunt.</p>
  <div class="avatar" role="img" aria-label="Client portrait"></div>
</article>

<section class="blog">
  <div class="photo" role="img" aria-label="Hospital ward interior tinted teal and blue"></div>
  <h2 class="sec-title" style="top:65px;font-size:38px;color:#fff">From The Blog</h2>
  <article class="blog-card" style="left:145px;top:162px">
    <div class="photo-s tone-lab" role="img" aria-label="Nurse helping an elderly patient walk"></div>
    <div class="date">OCT<br>2020</div>
    <h3>NEMO ENIM IPSAM VOLUPTATEM QUIA VOLUPTAS SIT</h3>
    <p>Lorem ipsum dolor sit amet, contetur adipiscing elit, sed do eiusmod mpor incididunt ut labore et dolore magna aliqua. Ut enim ad minim</p>
    <span class="more">READ MORE ➔</span>
  </article>
  <article class="blog-card" style="left:457px;top:178px">
    <div class="photo-s tone-white" role="img" aria-label="Scientist working in a laboratory"></div>
    <div class="date">OCT<br>2020</div>
    <h3>NEMO ENIM IPSAM VOLUPTATEM QUIA VOLUPTAS SIT</h3>
    <p>Lorem ipsum dolor sit amet, contetur adipiscing elit, sed do eiusmod mpor incididunt ut labore et dolore magna aliqua. Ut enim ad minim</p>
    <span class="more">READ MORE ➔</span>
  </article>
  <article class="blog-card" style="left:768px;top:162px">
    <div class="photo-s tone-room" role="img" aria-label="Nurse taking a blood sample from a patient"></div>
    <div class="date">OCT<br>2020</div>
    <h3>NEMO ENIM IPSAM VOLUPTATEM QUIA VOLUPTAS SIT</h3>
    <p>Lorem ipsum dolor sit amet, contetur adipiscing elit, sed do eiusmod mpor incididunt ut labore et dolore magna aliqua. Ut enim ad minim</p>
    <span class="more">READ MORE ➔</span>
  </article>
  <svg class="abs" style="left:0;top:740px" width="1200" height="120" viewBox="0 0 1200 120" preserveAspectRatio="none">
    <path d="M0 80 C250 20 520 10 760 40 C950 65 1100 70 1200 55 L1200 120 L0 120Z" fill="#f3f4f6"/>
    <path d="M0 72 C250 12 520 2 760 32 C950 57 1100 62 1200 47" fill="none" stroke="#0455a3" stroke-width="4"/>
  </svg>
</section>

<footer class="site-footer">
  <div class="brand" style="left:145px;top:40px;font-size:40px"><span class="mark"></span>Lumora</div>
  <div class="field" style="top:142px">Name</div>
  <div class="field" style="top:191px">Email</div>
  <div class="btn" style="left:145px;top:242px;width:113px;height:36px;border-radius:2px;background:var(--forest);color:#fff;font-size:12px">Submit</div>

  <h4 class="foot-h" style="left:470px;top:32px">CONTACT US</h4>
  <div class="contact-row" style="top:72px"><svg width="14" height="18" viewBox="0 0 24 30"><path d="M12 0a10 10 0 00-10 10c0 8 10 20 10 20s10-12 10-20A10 10 0 0012 0z" fill="#0c4b52"/><circle cx="12" cy="10" r="4" fill="#fff"/></svg><div>Lumora<br>20 enim ipsam voluptatem<br>quia voluptas sit</div></div>
  <div class="contact-row" style="top:140px"><svg width="14" height="14" viewBox="0 0 24 24"><path fill="#0c4b52" d="M6.6 10.8a15 15 0 006.6 6.6l2.2-2.2a1 1 0 011-.25 11.4 11.4 0 003.6.57 1 1 0 011 1V20a1 1 0 01-1 1A17 17 0 013 4a1 1 0 011-1h3.5a1 1 0 011 1c0 1.25.2 2.45.57 3.57a1 1 0 01-.25 1z"/></svg><div>Phone:<br>555 0190 4421</div></div>
  <div class="contact-row" style="top:192px"><svg width="16" height="12" viewBox="0 0 24 18"><rect width="24" height="18" fill="#0c4b52"/><path d="M0 0l12 9 12-9" stroke="#fff" stroke-width="2" fill="none"/></svg><div>Email:<br>hello@lumora-care.com</div></div>

  <h4 class="foot-h" style="left:755px;top:28px">QUICK LINKS</h4>
  <ul class="foot-list" style="left:760px;top:68px"><li>Home</li><li>About Us</li><li>Treatment</li><li>Our Services</li><li>Supplement</li><li>Contact Us</li></ul>

  <h4 class="foot-h" style="left:945px;top:28px">SOCIAL</h4>
  <ul class="social" style="top:62px"><li><i></i>Friendsy</li><li><i></i>Chirper</li><li><i></i>Searchly</li><li><i></i>Vidstream</li></ul>
</footer>

<p class="copyright">Lumora © 2020 All Rights Reserved | Privacy Policy | Terms and Conditions</p>

</body>
</html>
```